Florabelle Packaging Design Project Hair Removal products

Florabelle is launching a New Hair Removal Sub Brand, under the Florabelle Brand .

This new hair removal range will include approx six products that are all designed to remove hair. These include hot wax, wax strips, depilitaory creams, hair removal lotion etc.

We are looking for a fresh new look and a sub brand name for the range. Currently we have a name Florabelle Sorbet Swish as a name option but we are not sold on this name so we would like to see other options . We would like the brand to use the same primary colours as our current florabelle brand. ie the pink and the blue but it should look different from the current range. I will email through all the pantones and logos on the brand. You can check out florabelle-example.co.za to see the current range

For the design we would like to see a design for a sticker that goes on a bottle as well as see how it translates on a box.

Target Market(s)

any female using hair removal products

Industry/Entity Type

Hair

Requirements
Must have
• simple design.

must use our colours

it must somehow portray that using our hair removal system is really quick, easy and effective

You can use images of legs on the packaging but it is not required.

all design must have the main brand logo "Florabelle" on the packaging but with regard to the sub name for the brand we are not sold on our name so we require that for one of your artwork options that you use our name "Sorbet Swish" for one of the designs , however we would also like you to come up with your own name for the hair removal range.

Florabelle logo is not dominant and can remain in the background.

```html
<!DOCTYPE html>
<html lang="en">
<head>
<meta charset="utf-8">
<title>Florabelle Sorbet Swish – Box Dieline</title>
<link rel="stylesheet" href="https://fonts.googleapis.com/css2?family=Raleway:wght@200;400&display=swap">
<style>
  :root {
    --bg: #e4e4e4;
    --bg-light: #f4f4f4;
    --board: #ffffff;
    --cut-line: #c8c8c8;
    --pink: #e8237d;
    --pink-soft: #f5b9d6;
    --pink-pale: #fbe3ef;
    --skin: #f1d2c2;
  }
  html, body {
    margin: 0;
    padding: 0;
    width: 1200px;
    height: 901px;
    overflow: hidden;
    background: var(--bg);
  }
  .stage {
    display: block;
    width: 1200px;
    height: 901px;
  }
  .board { fill: var(--board); stroke: var(--cut-line); stroke-width: 1; }
  .brand-name {
    font-family: "Raleway", sans-serif;
    font-weight: 400;
    fill: var(--pink);
  }
  .brand-dot { fill: var(--pink); }
  .range-name {
    font-family: "Raleway", sans-serif;
    font-weight: 200;
    fill: var(--pink);
  }
  .range-type {
    font-family: "Raleway", sans-serif;
    font-weight: 400;
    fill: var(--pink);
  }
  .end-band { fill: var(--pink); }
</style>
</head>
<body>
<svg class="stage" viewBox="0 0 1200 901" xmlns="http://www.w3.org/2000/svg">
  <defs>
    <radialGradient id="bg-glow" cx="0.7" cy="0.25" r="0.8">
      <stop offset="0" stop-color="var(--bg-light)"/>
      <stop offset="1" stop-color="var(--bg)"/>
    </radialGradient>
    <radialGradient id="flower-tone" cx="0.45" cy="0.6" r="0.6">
      <stop offset="0" stop-color="#ee8dbb"/>
      <stop offset="0.45" stop-color="#f7c7de"/>
      <stop offset="1" stop-color="#ffffff" stop-opacity="0"/>
    </radialGradient>
    <linearGradient id="legs-tone" x1="0" x2="1" y1="0" y2="0">
      <stop offset="0" stop-color="var(--skin)"/>
      <stop offset="0.75" stop-color="var(--skin)"/>
      <stop offset="1" stop-color="var(--skin)" stop-opacity="0"/>
    </linearGradient>

    <g id="front-panel-text">
      <text class="brand-name" x="332" y="38" font-size="15" text-anchor="end">Florabelle</text>
      <circle class="brand-dot" cx="341" cy="33" r="4.5"/>
      <text class="range-name" x="350" y="96" font-size="36" text-anchor="end" textLength="205" lengthAdjust="spacingAndGlyphs">Sorbet Swish</text>
      <text class="range-type" x="350" y="114" font-size="9" text-anchor="end">Hair Removal</text>
    </g>
  </defs>

  <rect width="1200" height="901" fill="url(#bg-glow)"/>

  <g class="dieline" transform="translate(237 62)">
    <!-- side flaps -->
    <polygon class="board" points="203,233 105,258 105,356 203,380"/>
    <polygon class="board" points="569,233 674,258 674,356 569,380"/>
    <polygon class="board" points="203,530 105,555 105,653 203,677"/>
    <polygon class="board" points="569,530 674,555 674,653 569,677"/>
    <!-- bottom tuck flap -->
    <polygon class="board" points="203,677 218,711 554,711 569,677"/>

    <!-- right end panel -->
    <g class="end-panel end-panel--right">
      <rect class="board" x="569" y="81" width="123" height="152"/>
      <g transform="translate(616 110) rotate(90)">
        <text class="brand-name" x="0" y="0" font-size="18">Florabelle</text>
        <circle class="brand-dot" cx="96" cy="-6" r="5"/>
      </g>
    </g>

    <!-- left end panel -->
    <g class="end-panel end-panel--left">
      <rect class="board" x="33" y="380" width="170" height="150"/>
      <rect class="end-band" x="33" y="380" width="170" height="12"/>
      <g transform="translate(90 405) rotate(90)">
        <text class="brand-name" x="0" y="0" font-size="18">Florabelle</text>
        <circle class="brand-dot" cx="96" cy="-6" r="5"/>
      </g>
    </g>

    <!-- panel 1: front with legs -->
    <g class="face face--front" transform="translate(203 81)">
      <rect class="board" width="366" height="152"/>
      <rect role="img" aria-label="Soft pink lotus flower illustration" x="0" y="0" width="150" height="152" fill="url(#flower-tone)"/>
      <rect role="img" aria-label="Illustration of smooth bare legs" x="0" y="72" width="135" height="26" rx="12" fill="url(#legs-tone)"/>
      <use href="#front-panel-text"/>
    </g>

    <!-- panel 2: flower only -->
    <g class="face face--side" transform="translate(203 233)">
      <rect class="board" width="366" height="147"/>
      <rect role="img" aria-label="Soft pink lotus flower illustration" x="0" y="0" width="150" height="147" fill="url(#flower-tone)"/>
      <use href="#front-panel-text"/>
    </g>

    <!-- panel 3: back with legs -->
    <g class="face face--back" transform="translate(203 380)">
      <rect class="board" width="366" height="150"/>
      <rect role="img" aria-label="Soft pink lotus flower illustration" x="0" y="0" width="150" height="150" fill="url(#flower-tone)"/>
      <rect role="img" aria-label="Illustration of smooth bare legs" x="0" y="72" width="135" height="26" rx="12" fill="url(#legs-tone)"/>
      <use href="#front-panel-text"/>
    </g>

    <!-- panel 4: flower only -->
    <g class="face face--side" transform="translate(203 530)">
      <rect class="board" width="366" height="147"/>
      <rect role="img" aria-label="Soft pink lotus flower illustration" x="0" y="0" width="150" height="147" fill="url(#flower-tone)"/>
      <use href="#front-panel-text"/>
    </g>
  </g>
</svg>
</body>
</html>
```